Super elegant, crisp & clean Business card design required

We recently upgraded our branding - which is on our website - tavorelstudio.com

I would like a simple, yet elegant, clean business card design please.

The font of my logo is Cinzel - and because of the natural colour - it's best to have this on a black background.

I would like to have the back of the business card - with simply my logo.

PLEASE DO NOT SUBMIT A COMPLICATED / UNCLEAN DESIGN

Industry/Entity Type

Business

Contact Information for Business Card

Dalvik Ostrander Photography

Font styles to use
Other font styles liked:
• Cinzel

Requirements
Must have
• A backpage with nothing but my logo
• Simple design - stands out
Should not have
• Colour that dont align with my logo
• Over complicated '/ non symmetrical design

```html
<!DOCTYPE html>
<html lang="en">
<head>
<meta charset="utf-8">
<title>Dalvik Ostrander Photography — Business Card</title>
<link rel="stylesheet" href="https://fonts.googleapis.com/css2?family=Cinzel:wght@400&family=Montserrat:wght@400&display=swap">
<style>
  :root {
    --backdrop: #3a302b;
    --card: #141414;
    --card-edge: #1c1c1c;
    --gold: #8a7a62;
    --gold-soft: #6f624f;
    --ink-light: #e6e6e6;
  }
  * { box-sizing: border-box; margin: 0; padding: 0; }
  html, body {
    width: 1200px; height: 864px; overflow: hidden;
    background: var(--backdrop);
  }
  .stage { position: relative; width: 1200px; height: 864px; }
  .card {
    position: absolute;
    width: 530px; height: 303px;
    background: var(--card);
    border: 1px solid var(--card-edge);
    box-shadow: 0 18px 40px rgba(0,0,0,0.45);
    display: flex; flex-direction: column; align-items: center; justify-content: center;
    text-align: center;
  }
  .card--back { left: 70px; top: 110px; }
  .card--front { left: 600px; top: 420px; }

  .brand-mark {
    width: 46px; height: 46px; border-radius: 50%;
    border: 1.5px solid var(--gold);
    margin-bottom: 16px;
  }
  .brand-name {
    font-family: "Cinzel", serif; font-weight: 400;
    color: var(--gold);
    font-size: 25px; letter-spacing: 0.02em; line-height: 1;
  }
  .brand-line {
    font-family: "Cinzel", serif; font-weight: 400;
    color: var(--gold);
    font-size: 11px; letter-spacing: 0.62em; margin-top: 6px; padding-left: 0.62em;
  }
  .social {
    position: absolute; right: 18px; top: 110px;
    display: flex; align-items: center; gap: 5px;
    font-family: "Cinzel", serif; font-size: 9px; color: var(--gold-soft);
  }
  .social-square { width: 12px; height: 12px; background: var(--gold-soft); }

  .card--front .brand-mark { width: 40px; height: 40px; margin-bottom: 12px; }
  .card--front .brand-name { font-size: 21px; }
  .card--front .brand-line { font-size: 9.5px; }
  .contact {
    margin-top: 22px;
    font-family: "Montserrat", sans-serif; font-size: 13.5px;
    color: var(--ink-light); line-height: 1.5;
  }
</style>
</head>
<body>
<main class="stage">
  <section class="card card--back" aria-label="Card back">
    <div class="brand-mark" aria-hidden="true"></div>
    <div class="brand-name">Dalvik Ostrander</div>
    <div class="brand-line">Photography</div>
    <div class="social"><span class="social-square"></span><span>Folionet</span></div>
  </section>

  <section class="card card--front" aria-label="Card front">
    <div class="brand-mark" aria-hidden="true"></div>
    <div class="brand-name">Dalvik Ostrander</div>
    <div class="brand-line">Photography</div>
    <div class="contact">
      <p>07946210583 | info@tavorelstudio.com</p>
      <p>www.tavorelstudio.com</p>
    </div>
  </section>
</main>
</body>
</html>
```